High End Business Card Design for Flooring Store

Looking for a new card design for our hardwood flooring company. We have no print budget for these and are open to cards made from wood, metal, cardstock with embossed print ... or any combination of these. No plastic.

We sell luxury products and I want the cards to reflect our image of quality and class.

Our contact information as such;
Employee Name
418 Colbrook Blvd.
Marlow, NB
K9R-3M5
(555) 214-3968
Employee email @velkaflooring.com

Target Market(s)

Home Builders

Contact Information for Business Card

Emnployee name, business contact information

```html
<!DOCTYPE html>
<html lang="en">
<head>
<meta charset="utf-8">
<title>Velka Flooring – Business Card</title>
<link href="https://fonts.googleapis.com/css2?family=Montserrat:wght@400;500;600;700&display=swap" rel="stylesheet">
<style>
  :root {
    --brand-red: #97281f;
    --brand-gold: #e9b020;
    --ink: #1c1c1c;
    --tagline-grey: #7a7a7a;
    --card-white: #ffffff;
    --backdrop: #e6e6e6;
  }
  * { margin: 0; padding: 0; box-sizing: border-box; }
  html, body {
    width: 1200px; height: 874px; overflow: hidden;
    background: var(--backdrop);
    font-family: "Montserrat", sans-serif;
  }
  .canvas { position: relative; width: 1200px; height: 874px; }
  .card {
    position: absolute; left: 250px; width: 700px; height: 400px;
    background: var(--card-white); border-radius: 22px; overflow: hidden;
    box-shadow: 0 6px 18px rgba(0,0,0,0.18);
  }
  .card--front { top: 24px; }
  .card--back { top: 450px; }

  .brand { display: flex; align-items: center; gap: 14px; }
  .brand__square { background: var(--brand-gold); flex: none; }
  .brand__name { color: var(--brand-red); font-weight: 500; line-height: 1; letter-spacing: -1px; }
  .brand__tagline { color: var(--tagline-grey); font-weight: 500; line-height: 1.1; }

  .card--front .brand-lockup {
    position: absolute; left: 0; right: 0; top: 95px;
    display: flex; flex-direction: column; align-items: center;
  }
  .card--front .brand__square { width: 52px; height: 52px; }
  .card--front .brand__name { font-size: 136px; }
  .card--front .brand__tagline { font-size: 31px; text-align: center; margin-top: 6px; margin-left: 40px; }

  .card--back .brand-lockup { position: absolute; left: 46px; top: 118px; }
  .card--back .brand__square { width: 26px; height: 26px; }
  .card--back .brand__name { font-size: 66px; }
  .card--back .brand__tagline { font-size: 16px; margin-left: 40px; margin-top: 4px; }

  .divider {
    position: absolute; left: 340px; top: 100px; width: 2px; height: 200px;
    background: var(--brand-gold);
  }
  .contact { position: absolute; left: 372px; top: 110px; color: var(--ink); }
  .contact__name { font-size: 29px; font-weight: 700; color: var(--brand-gold); line-height: 1; }
  .contact__name-last { color: var(--brand-red); }
  .contact__role { font-size: 18px; margin: 6px 0 10px; }
  .contact__address { font-size: 18px; line-height: 1.3; font-style: normal; }
  .contact__lines { list-style: none; margin-top: 10px; font-size: 18px; line-height: 1.4; }
  .contact__lines li { display: flex; align-items: center; gap: 8px; }
  .contact__lines svg { width: 14px; height: 14px; fill: var(--brand-gold); flex: none; }

  .swoosh { position: absolute; left: 0; top: 0; width: 700px; height: 400px; }
</style>
</head>
<body>
<main class="canvas">

  <section class="card card--front" aria-label="Card front">
    <div class="brand-lockup">
      <div class="brand">
        <span class="brand__square"></span>
        <span class="brand__name">Velka</span>
      </div>
      <p class="brand__tagline">Planchers &amp; Escaliers<br>Flooring &amp; Stairs</p>
    </div>
  </section>

  <section class="card card--back" aria-label="Card back">
    <svg class="swoosh" viewBox="0 0 700 400" aria-hidden="true">
      <path d="M300 352 C420 398 560 398 700 368 L700 394 C560 408 420 404 300 352 Z" fill="var(--brand-gold)"/>
      <path d="M0 328 C120 300 260 318 400 376 C430 388 450 396 470 400 L0 400 Z" fill="var(--brand-red)"/>
      <path d="M0 314 C130 284 270 304 420 370" fill="none" stroke="var(--brand-red)" stroke-width="3"/>
    </svg>

    <div class="brand-lockup">
      <div class="brand">
        <span class="brand__square"></span>
        <span class="brand__name">Velka</span>
      </div>
      <p class="brand__tagline">Planchers &amp; Escaliers<br>Flooring &amp; Stairs</p>
    </div>

    <div class="divider"></div>

    <div class="contact">
      <h1 class="contact__name">Employee <span class="contact__name-last">Name</span></h1>
      <p class="contact__role">Owner/CEO</p>
      <address class="contact__address">418 Colbrook Blvd.<br>Marlow, NB<br>K9R-3M5</address>
      <ul class="contact__lines">
        <li><svg viewBox="0 0 16 16"><path d="M3 1h3l1.5 4-2 1.2a9 9 0 0 0 4.3 4.3L11 8.5l4 1.5v3a2 2 0 0 1-2 2A12 12 0 0 1 1 3a2 2 0 0 1 2-2z"/></svg>(555) 214-3968</li>
        <li><svg viewBox="0 0 16 16"><path d="M1 3h14v10H1z M1 3l7 6 7-6" fill="none" stroke="var(--brand-gold)" stroke-width="1.8"/></svg>info@velkaflooring.com</li>
        <li><svg viewBox="0 0 16 16"><circle cx="8" cy="8" r="7" fill="none" stroke="var(--brand-gold)" stroke-width="1.6"/><path d="M1 8h14M8 1c-3 4-3 10 0 14M8 1c3 4 3 10 0 14" fill="none" stroke="var(--brand-gold)" stroke-width="1.2"/></svg>www.velkaflooring.com</li>
      </ul>
    </div>
  </section>

</main>
</body>
</html>
```